Business Card Design for Small Electrical Contractor

I need to update my business card into something a little more modern. We are a small electrical contracting company. We service domestic and commercial places around Sydney. We have 2 logo designs at the moment. I have uploaded both and 2 different sizes to work with.

Industry/Entity Type

Business

Contact Information for Business Card

Leo Hartigan
8/21-23 Birch Rd, Kelsworth 2087
t - (02) 9381 4720
m - 0427 815 903
E - info@hartiganelx.com.au
W - hartiganelx.com.au
ABN: 42 907 551 316

Font styles to use
Sans Serif

Requirements
Must have
• I would also like to see the below fit on somewhere aswell
• - Licensed Electrician
• - Level 2 (Cat 1 & 4)
• - Domestic
• - Commercial
• - Repairs and Installations
• - Data
Nice to have
• Try and keep similar colours as logo
Should not have
• No lightning bolts or light globes. Smart and professional please.

```html
<!DOCTYPE html>
<html lang="en">
<head>
<meta charset="utf-8">
<title>L&amp;R Hartigan Electrical — Business Card</title>
<link rel="stylesheet" href="https://fonts.googleapis.com/css2?family=Source+Sans+3:ital,wght@0,400;0,600;1,400&display=swap">
<style>
  :root {
    --backdrop: #8f9092;
    --card: #eceef0;
    --ink-dark: #02272b;
    --accent: #d9831f;
    --text: #3a3d40;
    --text-soft: #4a4d50;
    --white: #ffffff;
  }
  * { margin: 0; padding: 0; box-sizing: border-box; }
  html, body {
    width: 1105px; height: 1200px; overflow: hidden;
    background: var(--backdrop);
    font-family: "Source Sans 3", "Myriad Pro", sans-serif;
  }
  .canvas { position: relative; width: 1105px; height: 1200px; }

  .card {
    position: absolute; left: 178px; width: 748px; height: 426px;
    background: var(--card); overflow: hidden;
  }
  .card--front { top: 120px; }
  .card--back { top: 654px; }

  /* Front */
  .brand-band {
    height: 192px; background: var(--ink-dark);
    display: flex; align-items: center; justify-content: center;
  }
  .wordmark {
    font-family: "Source Sans 3", sans-serif;
    font-weight: 600; font-size: 42px; letter-spacing: 1px;
    white-space: nowrap;
  }
  .brand-band .wordmark { color: var(--white); }

  .details { position: relative; height: 198px; }
  .holder { position: absolute; top: 20px; left: 0; right: 0; text-align: center; }
  .holder__name { font-weight: 600; font-size: 26px; color: var(--ink-dark); line-height: 1.2; }
  .holder__role { font-size: 19px; color: var(--accent); line-height: 1.3; }

  .contact-list {
    position: absolute; left: 39px; top: 88px; list-style: none;
    font-size: 19px; color: var(--text);
  }
  .contact-list li { display: flex; align-items: center; height: 27.5px; }
  .contact-list svg { width: 18px; height: 18px; margin-right: 11px; flex: none; fill: var(--ink-dark); }

  .address {
    position: absolute; right: 39px; top: 88px; text-align: right;
    font-style: normal; font-size: 19px; color: var(--text); line-height: 27.5px;
  }

  .web-bar {
    height: 36px; background: var(--accent);
    display: flex; align-items: center; justify-content: center;
    color: var(--white); font-size: 20px; letter-spacing: 2px;
  }

  /* Back */
  .back-brand {
    position: absolute; top: 160px; left: 0; right: 0; text-align: center;
  }
  .back-brand .wordmark { color: var(--ink-dark); }
  .services {
    position: absolute; top: 318px; left: 0; right: 0; text-align: center;
    font-style: italic; font-size: 20px; color: var(--text-soft); line-height: 27px;
  }
  .services .dot { font-style: normal; color: var(--ink-dark); margin: 0 6px; }
</style>
</head>
<body>
<main class="canvas">

  <section class="card card--front" aria-label="Business card front">
    <header class="brand-band">
      <span class="wordmark">L&amp;R Hartigan Electrical</span>
    </header>

    <div class="details">
      <div class="holder">
        <p class="holder__name">Leo Hartigan</p>
        <p class="holder__role">Licensed Electrician</p>
      </div>

      <ul class="contact-list">
        <li>
          <svg viewBox="0 0 24 24" aria-hidden="true"><path d="M6.6 10.8a15.1 15.1 0 0 0 6.6 6.6l2.2-2.2a1 1 0 0 1 1-.25 11.4 11.4 0 0 0 3.6.57 1 1 0 0 1 1 1V20a1 1 0 0 1-1 1A17 17 0 0 1 3 4a1 1 0 0 1 1-1h3.5a1 1 0 0 1 1 1c0 1.25.2 2.45.57 3.57a1 1 0 0 1-.25 1z"/></svg>
          (02) 9381 4720
        </li>
        <li>
          <svg viewBox="0 0 24 24" aria-hidden="true"><path d="M7 1h10a2 2 0 0 1 2 2v18a2 2 0 0 1-2 2H7a2 2 0 0 1-2-2V3a2 2 0 0 1 2-2zm0 3v14h10V4zm5 15.2a1.2 1.2 0 1 0 0 2.4 1.2 1.2 0 0 0 0-2.4z"/></svg>
          0427 815 903
        </li>
        <li>
          <svg viewBox="0 0 24 24" aria-hidden="true"><path d="M2 5h20v14H2zm2 2v.5l8 5 8-5V7zm0 2.9V17h16V9.9l-8 5z"/></svg>
          info@hartiganelx.com.au
        </li>
      </ul>

      <address class="address">
        8/21-23 Birch Rd<br>
        Kelsworth 2087<br>
        ABN: 42 907 551 316
      </address>
    </div>

    <footer class="web-bar">www.hartiganelx.com.au</footer>
  </section>

  <section class="card card--back" aria-label="Business card back">
    <div class="back-brand">
      <span class="wordmark">L&amp;R Hartigan Electrical</span>
    </div>
    <p class="services">
      Level 2 (Cat 1 &amp; 4)<span class="dot">●</span>Domestic<span class="dot">●</span>Commercial<br>
      Repairs &amp; Installations<span class="dot">●</span>Data
    </p>
  </section>

</main>
</body>
</html>
```